Postcard Design

Roofing and Construction Company.

I have included our logo and a brief outline of what I want on our postcard. We are attempting to get our name and logo recognition in the roofing industry in the Tampa Florida area.

Logo colors need to match as well as other colors in the postcard I would like the same orange in various places.

Industry/Entity Type

Roofing

Font styles to use
Serif

Requirements
Must have
• Priorities are "Up to $500 off a new roof system"

12 month 0% interest financing available

```html
<!DOCTYPE html>
<html lang="en">
<head>
<meta charset="utf-8">
<title>Gulfline Roofing Postcard</title>
<link href="https://fonts.googleapis.com/css2?family=Source+Serif+4:wght@400;700;900&display=swap" rel="stylesheet">
<style>
  :root {
    --panel-grey: #6d6e70;
    --paper: #ffffff;
    --ink-light: #ffffff;
    --line-grey: #cfd0d2;
    --stamp-border: #c9cacc;
    --brand-orange: #f08a3c;
  }
  * { box-sizing: border-box; margin: 0; padding: 0; }
  html, body { width: 1200px; height: 932px; overflow: hidden; background: var(--paper); }
  .postcard {
    position: relative;
    width: 1200px;
    height: 932px;
    background: var(--paper);
    font-family: "Source Serif 4", Georgia, serif;
  }
  .letter-panel {
    position: absolute;
    left: 0; top: 0;
    width: 620px; height: 932px;
    background: var(--panel-grey);
    color: var(--ink-light);
    padding: 32px 30px 0 34px;
    font-size: 15px;
    line-height: 22px;
  }
  .letter-panel p { margin-bottom: 18px; }
  .reasons { list-style: none; margin: -4px 0 18px; }
  .reasons li { position: relative; padding-left: 18px; }
  .reasons li::before {
    content: ""; position: absolute; left: 3px; top: 8px;
    width: 6px; height: 6px; border-radius: 50%; background: var(--brand-orange);
  }
  .reasons .offer { color: var(--brand-orange); font-weight: 700; }
  .signoff { margin-bottom: 0; }
  .signature { margin-top: 18px; }
  .brand-block {
    position: absolute;
    left: 0; width: 620px; top: 708px;
    text-align: center;
    color: var(--ink-light);
  }
  .brand-rule {
    width: 240px; height: 3px; margin: 0 auto 20px;
    background: var(--brand-orange);
  }
  .brand-name {
    display: inline-flex; align-items: center; gap: 10px;
    font-weight: 900; font-size: 23px; letter-spacing: 1px;
    text-transform: uppercase; margin-bottom: 12px;
  }
  .brand-mark { width: 16px; height: 16px; background: var(--brand-orange); }
  .contact-lines { font-weight: 700; font-size: 15px; line-height: 22px; }
  .contact-lines .label { color: var(--brand-orange); }
  .stamp-box {
    position: absolute; left: 962px; top: 74px;
    width: 196px; height: 204px;
    border: 2px solid var(--stamp-border);
  }
  .address-lines { position: absolute; left: 648px; top: 0; }
  .address-lines span {
    position: absolute; left: 0; width: 510px; height: 1px;
    background: var(--line-grey);
  }
</style>
</head>
<body>
<div class="postcard">
  <section class="letter-panel">
    <p>Dear Neighbor,</p>
    <p>Does your roof need to be repaired or replaced? If so, give me a call! We're currently working in your neighborhood, and we'd appreciate the opportunity to give you a free roof evaluation and show you our work.</p>
    <p>Here are a few reasons why now is the time to call:</p>
    <ul class="reasons">
      <li class="offer">Up to $500 off a new roof system;</li>
      <li>We are offering reduced pricing right now since we already have crews working in your neighborhood;</li>
      <li>We provide free wind mitigation reports with all new roofs – which could save you up to 15 percent on your homeowners insurance;</li>
      <li class="offer">12 month 0% interest financing available;</li>
      <li>And don't forget…hurricane season is right around the corner!</li>
    </ul>
    <p>Give us a call. You won't be disappointed with our professional service and competitive pricing.</p>
    <p>Thanks in advance for your time and consideration.</p>
    <p class="signoff">Sincerely,</p>
    <p class="signature">Dana Whitfield, Office Manager<br>PH:</p>
  </section>

  <div class="brand-block">
    <div class="brand-rule"></div>
    <div class="brand-name"><span class="brand-mark"></span>Gulfline Roofing</div>
    <div class="contact-lines">
      1450 S Harbor Road, Brandon, FL 33510<br>
      <span class="label">PH:</span> (813) 555-0142<br>
      <span class="label">FX:</span> (813) 555-0178<br>
      CCC1598432
    </div>
  </div>

  <div class="stamp-box" aria-label="Postage stamp area"></div>

  <div class="address-lines" aria-hidden="true">
    <span style="top:382px"></span>
    <span style="top:447px"></span>
    <span style="top:512px"></span>
    <span style="top:578px"></span>
    <span style="top:645px"></span>
    <span style="top:712px"></span>
  </div>
</div>
</body>
</html>
```